First Annual Pemberton Family Reunion

Family reunion invitation, please see the attached letter for the language. Also provided a picture of my grandparents, if you could include it on a letter or brochure. I'm flexible.
Updates

I just uploaded a Word document with the time, address, and list of activities. Please click on the hyperlink, it takes you directly to our Family Reunion webpage and click on Agenda for all details.

Target Market(s)

Family and Friends invitation

Requirements
Must have
• Date, time, picture, family logo, and website for payment

```html
<!DOCTYPE html>
<html lang="en">
<head>
<meta charset="utf-8">
<title>Pemberton Family Reunion 2023</title>
<link rel="stylesheet" href="https://fonts.googleapis.com/css2?family=Cinzel:wght@400;600;700&family=Tinos&display=swap">
<style>
  :root {
    --cream: #fdf9f6;
    --ink: #0d0a0b;
    --plum-deep: #64309a;
    --plum: #8e449f;
    --rose: #c95e98;
    --blush: #f4c7d6;
    --blush-soft: #f3dde6;
    --line-pink: #f2a3c8;
    --white: #ffffff;
    --link: #a8509a;
  }
  * { margin: 0; padding: 0; box-sizing: border-box; }
  html, body { width: 846px; height: 1200px; overflow: hidden; background: var(--cream); }
  .invite { position: relative; width: 846px; height: 1200px; background: var(--cream); font-family: "Cinzel", serif; color: var(--ink); overflow: hidden; }
  .backdrop { position: absolute; inset: 0; }

  .family-mark { position: absolute; left: 128px; top: 118px; width: 170px; display: flex; align-items: center; gap: 10px; }
  .family-mark__square { width: 22px; height: 22px; background: var(--ink); flex: none; }
  .family-mark__name { font-family: "Cinzel", serif; font-weight: 700; font-size: 19px; line-height: 1.15; letter-spacing: 0.5px; color: var(--ink); }

  .title-rule { position: absolute; left: 319px; width: 416px; height: 2px; background: var(--blush); }
  .title { position: absolute; left: 319px; top: 96px; width: 420px; font-weight: 700; line-height: 1; white-space: nowrap; }
  .title__family { display: block; font-size: 36px; letter-spacing: 0.5px; }
  .title__year { display: block; font-size: 51px; margin-top: 10px; letter-spacing: 0; }

  .activities { position: absolute; left: 134px; top: 270px; font-weight: 700; text-transform: uppercase; }
  .activities span { display: block; }
  .activities .small { font-size: 17px; line-height: 24px; letter-spacing: 0.8px; }
  .activities .big { font-size: 27px; line-height: 40px; letter-spacing: 0.8px; }
  .activities .mid { font-size: 24px; line-height: 31px; letter-spacing: 0.6px; }

  .photo { position: absolute; }
  .guide { position: absolute; background: var(--line-pink); }
  .guide--h { height: 2px; }
  .guide--v { width: 2px; }

  .dates { position: absolute; left: 264px; top: 860px; width: 320px; color: var(--white); }
  .date-row { position: relative; height: 48px; }
  .date-row__month, .date-row__year { position: absolute; top: 0; height: 46px; border-top: 2px solid var(--white); border-bottom: 2px solid var(--white); font-weight: 600; line-height: 42px; white-space: nowrap; }
  .date-row__month { left: 0; width: 156px; font-family: "Cinzel", serif; font-size: 24px; letter-spacing: 0; }
  .date-row__year { left: 248px; width: 69px; text-align: right; font-family: "Tinos", serif; font-weight: 400; font-size: 28px; }
  .date-row__day { position: absolute; left: 162px; top: -10px; font-family: "Tinos", serif; font-size: 74px; line-height: 64px; letter-spacing: -2px; }
  .dates__through { font-weight: 600; font-size: 25px; line-height: 50px; margin: 2px 0 2px 5px; letter-spacing: 1px; }

  .rsvp { position: absolute; left: 0; width: 846px; top: 1036px; text-align: center; color: var(--white); font-weight: 600; font-size: 25px; font-variant: small-caps; letter-spacing: 0.8px; white-space: nowrap; }
  .website { position: absolute; left: 250px; top: 1074px; width: 349px; height: 35px; background: var(--white); text-align: center; font-family: "Tinos", serif; font-size: 26px; line-height: 34px; color: var(--link); }
</style>
</head>
<body>
<main class="invite">
  <svg class="backdrop" width="846" height="1200" viewBox="0 0 846 1200" aria-hidden="true">
    <defs>
      <linearGradient id="cardFade" x1="0" y1="0" x2="0" y2="1">
        <stop offset="0" stop-color="#8a3f9f"/>
        <stop offset="0.6" stop-color="#aa509b"/>
        <stop offset="1" stop-color="#c95e98"/>
      </linearGradient>
      <linearGradient id="blushFade" x1="1" y1="0" x2="0" y2="1">
        <stop offset="0" stop-color="#f3dde6"/>
        <stop offset="1" stop-color="#e5a7c8"/>
      </linearGradient>
      <clipPath id="belowDiagonal"><polygon points="0,849 789,371 846,337 846,1200 0,1200"/></clipPath>
    </defs>
    <polygon points="789,342 789,371 0,849 0,848" fill="url(#blushFade)"/>
    <polygon points="789,342 846,330 846,337 0,849 0,846" fill="var(--blush-soft)" opacity="0.6"/>
    <polygon points="0,849 846,337 846,1200 0,1200" fill="var(--plum-deep)"/>
    <path d="M56 0 H789 V1088 Q789 1166 711 1166 H134 Q56 1166 56 1088 Z" fill="url(#cardFade)" clip-path="url(#belowDiagonal)"/>
  </svg>

  <div class="family-mark">
    <span class="family-mark__square"></span>
    <span class="family-mark__name">Pemberton Family Reunion</span>
  </div>

  <div class="title-rule" style="top:80px"></div>
  <h1 class="title">
    <span class="title__family">PEMBERTON FAMILY</span>
    <span class="title__year">REUNION 2023</span>
  </h1>
  <div class="title-rule" style="top:200px"></div>

  <p class="activities">
    <span class="small">Fun-filled</span>
    <span class="big">Weekend</span>
    <span class="small">with</span>
    <span class="big">Activities</span>
    <span class="small">for all ages,</span>
    <span class="small">which will</span>
    <span class="small">include</span>
    <span class="mid">Games, Music,</span>
    <span class="mid">Storytelling,</span>
    <span class="small">and much more.</span>
  </p>

  <div class="photo" role="img" aria-label="Photo of grandparents with a young grandchild, faded into the background" style="left:502px;top:831px;width:287px;height:335px;background:linear-gradient(160deg,rgba(230,170,200,0.3),rgba(150,70,130,0.15));"></div>

  <div class="guide guide--v" style="left:533px;top:212px;height:50px"></div>
  <div class="guide guide--h" style="left:313px;top:357px;width:216px"></div>
  <div class="guide guide--v" style="left:648px;top:264px;height:410px"></div>
  <div class="guide guide--h" style="left:136px;top:580px;width:622px"></div>
  <div class="guide guide--v" style="left:533px;top:580px;height:26px"></div>
  <div class="guide guide--h" style="left:149px;top:737px;width:78px"></div>
  <div class="guide guide--v" style="left:359px;top:580px;height:285px"></div>

  <div class="photo" role="img" aria-label="Family group photo in front of a television studio backdrop" style="left:402px;top:264px;width:126px;height:92px;background:linear-gradient(#3d5a8a,#5b4a48);"></div>
  <div class="photo" role="img" aria-label="Selfie of two relatives in a station hall" style="left:529px;top:264px;width:119px;height:157px;background:linear-gradient(#6a6660,#3a2a2c);"></div>
  <div class="photo" role="img" aria-label="Relatives gathered around a dinner table" style="left:361px;top:359px;width:167px;height:221px;background:linear-gradient(#c9b98e,#3a2626);"></div>
  <div class="photo" role="img" aria-label="Graduate in a blue cap and gown" style="left:529px;top:422px;width:119px;height:158px;background:linear-gradient(#e0a235,#2e63b8);"></div>
  <div class="photo" role="img" aria-label="Two cousins in matching red jackets on a park path" style="left:206px;top:584px;width:153px;height:153px;background:linear-gradient(#4d6a3a,#8a8078);"></div>
  <div class="photo" role="img" aria-label="Couple smiling together by a window" style="left:364px;top:584px;width:145px;height:196px;background:linear-gradient(#d89a54,#2b2a2c);"></div>
  <div class="photo" role="img" aria-label="Relative in a black graduation robe at home" style="left:226px;top:739px;width:133px;height:98px;background:linear-gradient(#d9d4c9,#2a2524);"></div>

  <section class="dates">
    <div class="date-row">
      <span class="date-row__month">SEPTEMBER</span>
      <span class="date-row__day">01</span>
      <span class="date-row__year">2023</span>
    </div>
    <p class="dates__through">THROUGH</p>
    <div class="date-row">
      <span class="date-row__month">SEPTEMBER</span>
      <span class="date-row__day">03</span>
      <span class="date-row__year">2023</span>
    </div>
  </section>

  <p class="rsvp">Please RSVP and pay your deposit as soon as possible</p>
  <p class="website">https://pembertonreunion.net</p>
</main>
</body>
</html>
```